family chiropractic health care team needs a modern business card design

Healthcare office with Chiropractors, Physiotherapists, Massage therapists and possibly other practitioners in the future. This is a friendly family office with patients of all ages (and lots of kids) that just moved into a new larger modern office.
Look at the website for photos of the office.
Design for the front and back of a business card required.
Text for the front:
Office logo and name of the office:
Bright Path Wellness Centre
Name of current Practitioner:
Dr. Marten Quovel B.Sc., D.C. Chiropractor
(But please include options to swap out name and title for other practitioners )

address:
218 Farrow Gate
Etobicoke ON.
K2J 6P4
Phone: 416-872-0196 (PATH)
Web site and email:
www.brightpathwellnesscentre.example
brightpathchiro@mailbox.example

2 versions of the back of the card:
1. text below
2. appointment schedule card

Text on back of card:
Chiropractic Card text on back of the card:
There is more to chiropractic than the relief of headaches and back pain! Our primary focus is the integrity of your nerve system, which controls and regulates every cell and tissue of your body. The moving bones of the spinal column can impair this vital communication link between your brain and body. We help improve the function and structure of your spine, reducing nerve system compromise. The result?
Even non-spinal related health problems can show improvement
without drugs
without surgery
regardless of age
for over a century
naturally

Appointment Card info For Back:
Please integrate design elements from the front of the card into an appointment card format.
M Tu W Th F Sat (and a line for writing on beside each one)

```html
<!DOCTYPE html>
<html lang="en">
<head>
<meta charset="utf-8">
<title>Bright Path Wellness Centre – Business Card</title>
<link rel="stylesheet" href="https://fonts.googleapis.com/css2?family=Questrial&display=swap">
<style>
  :root {
    --backdrop: #e4e4e4;
    --card-grey: #7f7d7d;
    --card-white: #ffffff;
    --brand-green: #8cc63f;
    --ink: #1e1e1e;
    --muted-grey: #8a8888;
    --rule: #2a2a2a;
  }
  * { box-sizing: border-box; margin: 0; padding: 0; }
  html, body {
    width: 1200px;
    height: 863px;
    overflow: hidden;
    background: var(--backdrop);
    font-family: "Questrial", "Century Gothic", sans-serif;
  }
  .sheet {
    width: 1200px;
    height: 863px;
    display: flex;
    align-items: center;
    justify-content: center;
    gap: 40px;
  }
  .card {
    position: relative;
    width: 540px;
    height: 309px;
    box-shadow: 0 6px 18px rgba(0,0,0,0.18);
    overflow: hidden;
  }

  /* Front */
  .card-front { background: var(--card-grey); color: var(--card-white); }
  .brand-band {
    position: absolute;
    left: 0; top: 62px;
    width: 100%; height: 116px;
    background: var(--card-white);
  }
  .brand-mark {
    position: absolute;
    left: 26px; top: 24px;
    display: flex;
    align-items: center;
    gap: 12px;
  }
  .brand-dot {
    width: 46px; height: 46px;
    border-radius: 50%;
    background: var(--brand-green);
    flex: none;
  }
  .brand-name {
    color: var(--brand-green);
    font-size: 27px;
    line-height: 1.05;
    letter-spacing: 0.5px;
    text-transform: uppercase;
  }
  .practitioner {
    position: absolute;
    right: 26px; top: 12px;
    text-align: center;
    color: var(--muted-grey);
  }
  .practitioner-name { font-size: 16px; }
  .practitioner-title { font-size: 9.5px; margin-top: 2px; }
  .contact {
    position: absolute;
    left: 150px; top: 190px;
    line-height: 1.3;
  }
  .contact-phone { font-size: 21px; letter-spacing: 0.5px; margin-bottom: 2px; }
  .contact-line { font-size: 14.5px; }

  /* Back */
  .card-back { background: var(--card-white); color: var(--ink); padding: 22px 30px; }
  .benefits-lead { font-size: 13px; }
  .benefits {
    list-style: none;
    font-size: 12.5px;
    line-height: 1.3;
    display: grid;
    grid-template-columns: auto auto;
    justify-content: start;
    column-gap: 18px;
  }
  .benefits li::before {
    content: "";
    display: inline-block;
    width: 0; height: 0;
    border-top: 4px solid transparent;
    border-bottom: 4px solid transparent;
    border-left: 7px solid var(--ink);
    margin-right: 7px;
  }
  .benefits .wide { grid-column: 1 / -1; }
  .divider { border: 0; border-top: 1px solid var(--rule); margin: 10px 0 12px; }
  .appointment-title { text-align: center; font-size: 18px; margin-bottom: 14px; }
  .weekdays { display: flex; justify-content: space-between; margin-bottom: 22px; }
  .day { display: flex; align-items: center; gap: 7px; font-size: 16px; }
  .day-box { width: 17px; height: 17px; border: 1px solid var(--ink); }
  .date-row { display: flex; align-items: flex-end; font-size: 16px; gap: 6px; }
  .write-line { flex: 1; border-bottom: 1px solid var(--rule); height: 14px; }
  .meridiem { font-size: 14px; line-height: 0.95; }
</style>
</head>
<body>
<main class="sheet">

  <section class="card card-front" aria-label="Business card front">
    <div class="brand-band">
      <div class="brand-mark">
        <span class="brand-dot"></span>
        <span class="brand-name">Bright Path<br>Wellness Centre</span>
      </div>
      <div class="practitioner">
        <p class="practitioner-name">Dr. Marten Quovel</p>
        <p class="practitioner-title">B.Sc., D.C. Chiropractor</p>
      </div>
    </div>
    <div class="contact">
      <p class="contact-phone">416-872-0196 (PATH)</p>
      <p class="contact-line">brightpathchiro@mailbox.example</p>
      <p class="contact-line">www.brightpathwellnesscentre.example</p>
      <p class="contact-line">218 Farrow Gate&nbsp; Etobicoke ON. K2J 6P4</p>
    </div>
  </section>

  <section class="card card-back" aria-label="Appointment card back">
    <p class="benefits-lead">Even non-spinal related health problems can show improvement</p>
    <ul class="benefits">
      <li>without drugs</li>
      <li>without surgery</li>
      <li class="wide">regardless of age for over a century</li>
      <li class="wide">naturally</li>
    </ul>
    <hr class="divider">
    <h2 class="appointment-title">Has An Appointment On</h2>
    <div class="weekdays">
      <span class="day"><span class="day-box"></span>Mon</span>
      <span class="day"><span class="day-box"></span>Tue</span>
      <span class="day"><span class="day-box"></span>Wed</span>
      <span class="day"><span class="day-box"></span>Thu</span>
      <span class="day"><span class="day-box"></span>Sat</span>
    </div>
    <div class="date-row">
      <span>Date</span>
      <span class="write-line"></span>
      <span>AT</span>
      <span class="write-line"></span>
      <span class="meridiem">am<br>pm</span>
    </div>
  </section>

</main>
</body>
</html>
```